Business Card for supplement company

Company Name: Brimcrest Nutrition
We require quite a simple yet stand out business card for our supplement company.
We are selling high end bodybuilding supplements direct to the public through online sales and Facebook marketing.
There will be slightly varying versions of the card and the winning design will be required to make these slight adjustments.
We will also require the file to be provided in and editable version as we will have a discount code on there that will be changed for different people.
Employee Cards:
Logo on the front of the card (see attached EPS file)
Please also add slogan in text "When Failure is Not and Option" as close as possible to what is seen in this link www.brimcrestnutrition.example.com.au
Suggestions: Card in black, possibly use a similar background to website theme (honeycomb, carbon look)
Information to be included on the back (please place and order accordingly)
:Tarq Welmsby (Director)
Email: tarq@brimcrestnutrition.example.com.au
Phone: 02 5918 2273
Website: www.brimcrestnutrition.example.com.au
Athlete Cards:
Front:
Same as above
Back:
Discount Code: xxx123 (to be editable)
Facebook: www.socialsite.example/BrimcrestNutrition
Design ideas: please look at our website and facebook signup page for design ideas.

```html
<!DOCTYPE html>
<html lang="en">
<head>
<meta charset="utf-8">
<title>Brimcrest Nutrition – Business Card</title>
<link rel="stylesheet" href="https://fonts.googleapis.com/css2?family=Exo+2:wght@400;600;700&display=swap">
<style>
  :root {
    --page-light: #ffffff;
    --page-shade: #d9d9d9;
    --card-black: #121212;
    --texture-dark: #1c1c1c;
    --texture-mid: #2a2a2a;
    --panel-black: #0b0b0b;
    --brand-green: #22d61e;
    --band-green-top: #00f000;
    --band-green-bottom: #006e00;
    --text-white: #f4f4f4;
    --icon-white: #e6e6e6;
  }
  * { margin: 0; padding: 0; box-sizing: border-box; }
  html, body {
    width: 1200px;
    height: 986px;
    overflow: hidden;
  }
  body {
    position: relative;
    background: radial-gradient(ellipse at 30% 45%, var(--page-light) 40%, var(--page-shade) 100%);
    font-family: "Exo 2", sans-serif;
  }
  .business-card {
    position: absolute;
    left: 84px;
    top: 168px;
    width: 1016px;
    height: 614px;
    background: var(--card-black);
    overflow: hidden;
  }
  .card-texture {
    position: absolute;
    inset: 0;
    background: radial-gradient(ellipse at 60% 20%, var(--texture-mid) 0%, var(--texture-dark) 55%, var(--card-black) 100%);
  }
  .accent-band {
    position: absolute;
    left: 0;
    top: 0;
    width: 182px;
    height: 100%;
    background:
      linear-gradient(90deg, rgba(0,0,0,0.18) 0%, rgba(0,0,0,0) 35%),
      linear-gradient(180deg, var(--band-green-top) 0%, #00c800 45%, var(--band-green-bottom) 100%);
  }
  .contact-panel {
    position: absolute;
    left: 150px;
    top: 292px;
    width: 866px;
    height: 306px;
    background: var(--panel-black);
    border-radius: 26px 0 0 26px;
  }
  .brand-name {
    position: absolute;
    left: 266px;
    top: 88px;
    width: 680px;
    text-align: center;
    color: var(--brand-green);
    font-weight: 700;
    font-size: 64px;
    line-height: 1;
    letter-spacing: 1px;
    text-transform: uppercase;
  }
  .brand-subline {
    position: absolute;
    left: 266px;
    top: 162px;
    width: 680px;
    text-align: center;
    color: var(--brand-green);
    font-weight: 700;
    font-size: 26px;
    letter-spacing: 7px;
    text-transform: uppercase;
  }
  .person {
    position: absolute;
    left: 178px;
    top: 306px;
    color: var(--text-white);
  }
  .person-name {
    font-size: 40px;
    font-weight: 400;
    line-height: 1.1;
    text-transform: uppercase;
  }
  .person-role {
    font-size: 30px;
    font-weight: 400;
    line-height: 1.3;
  }
  .contact-list {
    position: absolute;
    left: 178px;
    top: 440px;
    list-style: none;
    color: var(--text-white);
  }
  .contact-item {
    display: flex;
    align-items: center;
    height: 46px;
  }
  .contact-icon {
    width: 28px;
    height: 28px;
    margin-right: 14px;
    flex: none;
  }
  .contact-email { font-size: 26px; }
  .contact-phone { font-size: 32px; }
  .contact-web { font-size: 30px; }
</style>
</head>
<body>
  <section class="business-card" aria-label="Brimcrest Nutrition business card">
    <div class="card-texture" role="img" aria-label="Dark honeycomb carbon texture background"></div>
    <div class="accent-band"></div>
    <div class="contact-panel"></div>

    <p class="brand-name">Brimcrest</p>
    <p class="brand-subline">Nutrition</p>

    <div class="person">
      <p class="person-name">Tarq Welmsby</p>
      <p class="person-role">Director</p>
    </div>

    <ul class="contact-list">
      <li class="contact-item contact-email">
        <svg class="contact-icon" viewBox="0 0 28 28" aria-hidden="true">
          <rect x="2" y="7" width="24" height="15" fill="var(--icon-white)"/>
          <path d="M2 7 L14 16 L26 7" fill="none" stroke="var(--panel-black)" stroke-width="2"/>
        </svg>
        tarq@brimcrestnutrition.example.com.au
      </li>
      <li class="contact-item contact-phone">
        <svg class="contact-icon" viewBox="0 0 28 28" aria-hidden="true">
          <circle cx="14" cy="14" r="12" fill="none" stroke="var(--icon-white)" stroke-width="2"/>
          <path d="M9 7 C7 12 12 19 19 21 L21 18 L17 15 L15 17 C13 16 12 15 11 13 L13 11 L10 7 Z" fill="var(--icon-white)"/>
        </svg>
        02 5918 2273
      </li>
      <li class="contact-item contact-web">
        <svg class="contact-icon" viewBox="0 0 28 28" aria-hidden="true">
          <circle cx="14" cy="14" r="12" fill="var(--icon-white)"/>
          <path d="M7 9 C10 8 12 11 11 14 C10 17 8 17 7 20 M17 6 C16 9 19 11 21 10 M16 22 C17 19 20 18 22 17" fill="none" stroke="var(--panel-black)" stroke-width="2"/>
        </svg>
        www.brimcrestnutrition.example.com.au
      </li>
    </ul>
  </section>
</body>
</html>
```